Wordpress template re-design of current website

We need a WordPress template design and new look for our existing website. Our existing site it located at www.velmoro.com.au We are a tech company and want a fresh, clean modern website that matches our brand, services and logo colors. Our main Services are hospitality solutions, Velmoro TV solution and managed networks, more information on these can come from our existing website.

Target Market(s)

We are a tech company so must have a modern feel for new technology

Industry/Entity Type

It Company

Number of Pages Required

5+ page

Font styles to use
Sans Serif

Requirements
Must have
• Be based on a wordpress templete design and match the services that we have in our existing website, in the testimonials want a place for video testimonials as well as text. Nice clean icons used for graphics to represent services.
Nice to have
• nice visual representation of our services in the way of clean icons etc
Should not have
• Clutter

```html
<!DOCTYPE html>
<html lang="en">
<head>
<meta charset="utf-8">
<title>Velmoro Wireless</title>
<link href="https://fonts.googleapis.com/css2?family=Exo+2:wght@400;500;600&family=Roboto+Slab:wght@700&display=swap" rel="stylesheet">
<style>
:root{
  --navy:#0d3a7c;
  --blue:#3f8fe6;
  --blue-dark:#2266c8;
  --sky:#4faee0;
  --magenta:#c9469c;
  --brown:#5a2e2a;
  --teal:#4fb9b3;
  --grey-band:#f2f3f4;
  --text:#555b63;
  --white:#ffffff;
}
*{box-sizing:border-box;margin:0;padding:0}
html,body{width:1200px;height:2179px;overflow:hidden;background:#fff}
body{position:relative;font-family:"Exo 2",sans-serif;color:var(--text)}
.abs{position:absolute}

/* hero */
.hero{left:0;top:0;width:1200px;height:532px;background:linear-gradient(160deg,#b7a78a 0%,#6d6a62 30%,#2b3542 60%,#141c27 100%)}
.hero-welcome{left:132px;top:24px;font-size:13px;color:#e6e6e6}
.hero-phone{right:132px;top:20px;font-size:18px;color:#fff;font-weight:500}
.nav{left:132px;top:65px;width:936px;height:73px;background:#fff;border-radius:2px}
.brand{left:48px;top:18px;font-size:30px;font-weight:600;color:var(--blue-dark);display:flex;align-items:center;gap:8px}
.brand-dot{width:14px;height:14px;border-radius:50%;background:var(--navy)}
.nav-links{right:48px;top:20px;display:flex;gap:12px;font-size:13px;color:#222;align-items:center}
.nav-links span{padding:8px 12px;border:1px solid transparent}
.nav-links .active{border-color:#333}
.nav-links .portal{background:var(--blue);color:#fff}
.hero-rule{left:132px;top:271px;width:93px;height:5px;background:#111}
.hero-title{left:132px;top:290px;font-family:"Roboto Slab",serif;font-size:50px;color:#fff;letter-spacing:1px}
.hero-sub{left:132px;top:352px;font-size:25px;color:#fff}

/* intro */
.intro{left:0;top:585px;width:1200px;text-align:center;font-size:25px;line-height:30px;color:var(--navy)}
.intro em{font-style:normal;color:#4a5260}
.intro-rule{left:502px;top:677px;width:244px;height:3px;background:var(--navy)}
.intro-rule2{left:479px;top:680px;width:194px;height:5px;background:var(--blue)}

/* band */
.band{left:0;top:748px;width:1200px;height:124px;background:var(--grey-band);border-bottom:2px solid #bcd3f0}
.band-title{left:132px;top:780px;font-size:35px;font-weight:500;color:var(--navy)}
.band-sub{left:132px;top:817px;font-size:15px;color:#777}
.band-art{left:596px;top:697px;width:472px;height:160px;background:radial-gradient(ellipse at 75% 40%,rgba(210,60,60,.35),rgba(240,240,240,0) 65%)}

/* services */
.svc-icon{width:110px;height:110px;border-radius:50%}
.svc-title{font-size:23px;font-weight:500}
.svc-text{font-size:13.5px;line-height:16px;color:#777;width:290px}

/* ceo */
.ceo{left:0;top:1322px;width:1200px;height:334px;background:linear-gradient(100deg,#5c5651 0%,#44474c 45%,#3a4048 100%)}
.quote-badge{left:546px;top:1266px;width:108px;height:108px;border-radius:50%;background:var(--sky);border:5px solid #d7e9f5}
.ceo-title{left:0;top:1420px;width:1200px;text-align:center;font-size:24px;color:#fff}
.ceo-rule{left:372px;top:1473px;width:456px;height:1px;background:#c8c8c8}
.ceo-diamond{left:594px;top:1468px;width:10px;height:10px;background:var(--blue);transform:rotate(45deg)}
.ceo-text{left:200px;top:1536px;width:800px;text-align:center;font-size:13px;line-height:18px;color:#fff}
.dots{left:570px;top:1603px;display:flex;gap:8px}
.dots i{width:14px;height:3px;background:#fff}
.dots i.on{background:var(--blue)}

/* clients */
.clients-title{left:139px;top:1702px;font-size:23px;color:#fff;font-weight:500}
.client{top:1792px;font-size:24px;color:#333;font-weight:500;width:150px;text-align:center}
.clients-rule{left:132px;top:1857px;width:936px;height:2px;background:#b8d2f1}

/* footer */
.footer{left:0;top:1889px;width:1200px;height:239px;background:var(--blue)}
.footer-bar{left:0;top:2128px;width:1200px;height:51px;background:var(--blue-dark);text-align:center;line-height:51px;font-size:11px;color:#fff}
.f-head{top:1937px;font-size:18px;color:#fff}
.f-text{font-size:12.5px;line-height:15px;color:#0e3a78}
.f-list{font-size:13px;line-height:23px;color:#0e3a78}
.f-big{font-size:17px;color:#fff;line-height:25px}
.social{display:flex;gap:10px}
.social i{width:10px;height:10px;border-radius:50%;background:#fff}
</style>
</head>
<body>

<div class="abs hero" role="img" aria-label="Photo of a truck driving on an open highway at sunset"></div>
<div class="abs hero-welcome">Welcome to VELMORO WIRELESS</div>
<div class="abs hero-phone">(+00) 1300 555 014</div>
<nav class="abs nav">
  <div class="abs brand">Velmoro<span class="brand-dot"></span></div>
  <div class="abs nav-links">
    <span class="active">HOME</span><span>SERVICES</span><span>ABOUT</span><span>OUR WORK</span><span>CONTACT</span><span class="portal">PORTAL</span>
  </div>
</nav>
<div class="abs hero-rule"></div>
<h1 class="abs hero-title">VELMORO WIRELESS</h1>
<div class="abs hero-sub">Full Mobile 3G &amp; 4G Solutions</div>

<p class="abs intro">We strive to out work our competition <em>with an effective approach and a<br>powerful skill set,</em> which is why were industry leading.</p>
<div class="abs intro-rule"></div>
<div class="abs intro-rule2"></div>

<div class="abs band"></div>
<div class="abs band-art" role="img" aria-label="Illustration of a red rocket flying with a curved trail"></div>
<h2 class="abs band-title">VELMORO WIRELESS</h2>
<div class="abs band-sub">Creating solutions that work.</div>

<!-- services -->
<svg class="abs" style="left:143px;top:921px" width="110" height="110" viewBox="0 0 110 110">
  <circle cx="55" cy="55" r="55" fill="var(--sky)"/>
  <path d="M35 40a28 28 0 0 1 40 0M42 47a18 18 0 0 1 26 0M49 54a8 8 0 0 1 12 0" fill="none" stroke="#f5d22e" stroke-width="4" stroke-linecap="round"/>
  <rect x="28" y="62" width="54" height="16" rx="3" fill="#fff"/>
  <circle cx="70" cy="70" r="2.5" fill="#d33"/><circle cx="76" cy="70" r="2.5" fill="#d33"/>
</svg>
<svg class="abs" style="left:526px;top:921px" width="62" height="44"><polygon points="0,0 62,0 62,44" fill="var(--sky)"/></svg>
<div class="abs svc-title" style="left:292px;top:943px;color:var(--sky)">Wi-Fi Hotspots</div>
<div class="abs svc-text" style="left:292px;top:976px">Leading supplier of public access and internet billing systems.</div>

<svg class="abs" style="left:626px;top:921px" width="110" height="110" viewBox="0 0 110 110">
  <circle cx="55" cy="55" r="55" fill="var(--magenta)"/>
  <path d="M40 82V70c-8-6-10-14-8-22 3-12 16-18 28-14 10 3 14 12 13 20l5 8-5 2v6h-10v12z" fill="#fff"/>
  <ellipse cx="55" cy="47" rx="11" ry="8" fill="var(--magenta)"/>
  <circle cx="50" cy="47" r="1.6" fill="#fff"/><circle cx="55" cy="47" r="1.6" fill="#fff"/><circle cx="60" cy="47" r="1.6" fill="#fff"/>
</svg>
<svg class="abs" style="left:1004px;top:921px" width="64" height="44"><polygon points="0,0 64,0 64,44" fill="var(--magenta)"/></svg>
<div class="abs svc-title" style="left:771px;top:943px;color:var(--magenta)">HSIA Solutions</div>
<div class="abs svc-text" style="left:771px;top:976px">Our guest access solutions have been built with the guest in mind and are easy to use.</div>

<svg class="abs" style="left:143px;top:1097px" width="110" height="110" viewBox="0 0 110 110">
  <circle cx="55" cy="55" r="55" fill="var(--brown)"/>
  <path d="M45 30l10 10 10-10" fill="none" stroke="#ccc" stroke-width="2"/>
  <rect x="27" y="40" width="56" height="38" rx="5" fill="#f3a43a"/>
  <rect x="32" y="45" width="38" height="28" rx="3" fill="#9fd8e0"/>
  <circle cx="76" cy="51" r="2.5" fill="#5a2e2a"/><circle cx="76" cy="60" r="2.5" fill="#5a2e2a"/>
</svg>
<svg class="abs" style="left:526px;top:1097px" width="62" height="44"><polygon points="0,0 62,0 62,44" fill="var(--brown)"/></svg>
<div class="abs svc-title" style="left:292px;top:1116px;color:var(--brown)">Velmoro TV</div>
<div class="abs svc-text" style="left:292px;top:1150px">Turn you standard TV into a full guest information system and point of sale.</div>

<svg class="abs" style="left:626px;top:1097px" width="110" height="110" viewBox="0 0 110 110">
  <circle cx="55" cy="55" r="55" fill="var(--teal)"/>
  <circle cx="55" cy="44" r="7" fill="#fff"/><path d="M43 68a12 12 0 0 1 24 0z" fill="#fff"/>
  <circle cx="42" cy="52" r="5" fill="#fff"/><path d="M33 70a9 9 0 0 1 18 0z" fill="#fff"/>
  <circle cx="68" cy="52" r="5" fill="#fff"/><path d="M59 70a9 9 0 0 1 18 0z" fill="#fff"/>
</svg>
<svg class="abs" style="left:1004px;top:1097px" width="64" height="44"><polygon points="0,0 64,0 64,44" fill="var(--teal)"/></svg>
<div class="abs svc-title" style="left:771px;top:1116px;color:var(--teal)">Social Wi-Fi</div>
<div class="abs svc-text" style="left:771px;top:1150px">Get more out of your existing Wi-Fi with our social plug-ins to gain valuble insight into users.</div>

<!-- ceo -->
<div class="abs ceo" role="img" aria-label="Photo of two businessmen in conversation, darkened"></div>
<svg class="abs quote-badge" viewBox="0 0 98 98">
  <path d="M34 62l8-26h9l-6 26zM52 62l8-26h9l-6 26z" fill="#fff"/>
</svg>
<div class="abs ceo-title">CEO Message</div>
<div class="abs ceo-rule"></div>
<div class="abs ceo-diamond"></div>
<p class="abs ceo-text">Lorem ipsum dolor sit amet consectetur labore et dolore magna aliqua elit sed do eiusmod tempor ncididunt labore dolore magna aliqua minim aqula verana.Lorem ipsum dolor sit amet consectetur labore et dolore magna aliqua .</p>
<div class="abs dots"><i></i><i class="on"></i><i></i></div>

<!-- clients -->
<svg class="abs" style="left:132px;top:1692px" width="214" height="95"><polygon points="0,0 214,0 0,95" fill="var(--blue)"/></svg>
<h3 class="abs clients-title">Our Clients</h3>
<div class="abs client" style="left:167px">Norvane</div>
<div class="abs client" style="left:311px">Lodgeway</div>
<div class="abs client" style="left:450px">Ferrisk</div>
<div class="abs client" style="left:594px">Norvane</div>
<div class="abs client" style="left:738px">Lodgeway</div>
<div class="abs client" style="left:877px">Ferrisk</div>
<div class="abs clients-rule"></div>

<!-- footer -->
<footer>
<div class="abs footer"></div>
<div class="abs f-head" style="left:132px">About Us</div>
<p class="abs f-text" style="left:132px;top:1979px;width:285px">Velmoro Wireless has been a leader in wireless networks and internet billing systems for over a decade. Velmoro currently has completed over 2000 installations.</p>
<div class="abs f-text" style="left:132px;top:2055px;color:#fff">Read More..</div>

<div class="abs f-head" style="left:452px">Our&nbsp; Service</div>
<div class="abs f-list" style="left:452px;top:1974px">Case Studies<br>Testimonials<br>News<br>Resellers</div>

<div class="abs f-head" style="left:612px">Contact Info</div>
<div class="abs f-text" style="left:612px;top:1978px">48 Harbour Crescent<br>Coral Bay, QLD 4299</div>
<div class="abs f-big" style="left:612px;top:2017px">1300 555 014<br>sales@velmoro.com.au</div>

<div class="abs f-head" style="left:851px">Follow Us</div>
<div class="abs social" style="left:853px;top:1982px"><i aria-label="Social profile"></i><i aria-label="Social profile"></i></div>

<div class="abs footer-bar">© 2015 Velmoro Wireless. All Rights Reserved.</div>
</footer>
</body>
</html>
```